Ledgerwise Reach - B2B Demand Generation Website Project

We need a fully functional website for www.ledgerwisereach.example. We are a B2B Demand Generation company, based in London, working with companies such as QRT, VKD, Norvex, Brindlow, Tarvo generating them sales leads for their sales teams. We run this through digital marketing newsletter promotions and have a network of websites. Content syndication, data, demand generation, online marketing. Our logo has just been redone (attached) and we have a holding page already which i would like to use the style / colours. Our logo is bright and vibrant but i dont want the site to be a rainbow. We are expensive, classy, professorial, B2B, intelligent.

Home
About Us
Our Services
Prospora & QA Technology
Intent Data
Testimonials
Contact Us
Updates

Target Market(s)

B2B Marketers (QRT, Velquarion, Tarvo, VKD, Opal Reach, Driftmoor, Harlow Quantis, Technology Companies, Data Companies, Marketing Teams, Tumbleden.

Industry/Entity Type

Marketing

Coding

Coded - Design and coding required

Number of Pages Required

5+ page

Font styles to use
Sans Serif

Requirements
Must have
• Home
About Us
Our Services
Prospora & QA Technology
Intent Data
Testimonials
Contact Us

Simple Pages.

Look classy, intelligent, data experts. I like the video homepages were the image moves at the top. Very soft animation.
Nice to have
• Websites i like:

https://www.vkd.example/
https://www.brevantor.example/
https://www.plumfieldsites.example.co.uk/

Ledgerwise Reach - The Demand Generation Company
Should not have
• Glimpsevault crap images

```html
<!DOCTYPE html>
<html lang="en">
<head>
<meta charset="utf-8">
<title>Ledgerwise Reach - The Demand Generation Company</title>
<link rel="stylesheet" href="https://fonts.googleapis.com/css2?family=Montserrat:wght@400;500;600;700;800&family=Open+Sans:ital,wght@0,400;0,600;0,700;1,400&display=swap">
<style>
:root{
  --hero-a:#ff5b3a;
  --hero-b:#f0305e;
  --hero-c:#b51bd8;
  --blue:#1b74cc;
  --blue-dark:#1560ae;
  --navy:#163f73;
  --lavender:#ebebf8;
  --ink:#222633;
  --muted:#555a66;
  --line:#c9cbd6;
  --footer:#2b2b31;
  --white:#ffffff;
}
*{box-sizing:border-box;margin:0;padding:0}
html,body{width:1200px;height:4772px;overflow:hidden}
body{font-family:"Open Sans",sans-serif;color:var(--ink);background:var(--white);position:relative}
h1,h2,h3,.display{font-family:"Montserrat",sans-serif}
section,header,footer{position:relative;width:1200px}
.abs{position:absolute}
.btn{position:absolute;display:flex;align-items:center;justify-content:center;font-family:"Montserrat",sans-serif;font-weight:700;font-size:14px;color:var(--white);background:var(--blue-dark);border-radius:4px 4px 4px 4px;height:42px;width:142px;box-shadow:0 4px 0 var(--navy)}
.photo{position:absolute;border-top-right-radius:60px}
.frame{position:absolute;border:2px solid var(--line);border-top-right-radius:64px}

/* hero */
.hero{height:676px;background:linear-gradient(100deg,var(--hero-a) 0%,var(--hero-b) 40%,var(--hero-c) 100%);overflow:hidden}
.hero-curve{position:absolute;left:0;bottom:0;width:1200px;height:120px}
.brand{position:absolute;left:94px;top:30px;display:flex;align-items:center;gap:10px;color:var(--white)}
.brand-dot{width:36px;height:36px;border-radius:50%;border:3px solid var(--white)}
.brand-name{font-family:"Montserrat",sans-serif;font-weight:600;font-size:22px}
.brand-tag{position:absolute;left:46px;top:40px;font-size:8px;white-space:nowrap}
.nav{position:absolute;left:356px;top:52px;display:flex;gap:36px;font-family:"Montserrat",sans-serif;font-size:12px;font-weight:500;color:var(--white)}
.nav .active{border-bottom:2px solid var(--white);padding-bottom:6px}
.hero-kicker{position:absolute;left:94px;top:240px;font-family:"Montserrat",sans-serif;font-size:24px;color:var(--white)}
.hero-title{position:absolute;left:94px;top:270px;font-size:31px;font-weight:700;color:var(--white)}
.hero-text{position:absolute;left:94px;top:322px;width:560px;font-size:16px;line-height:23px;color:var(--white)}
.hero-btn{position:absolute;top:393px;height:42px;width:140px;display:flex;align-items:center;justify-content:center;font-family:"Montserrat",sans-serif;font-weight:700;font-size:14px;border-radius:4px}
.hero-btn.solid{left:94px;background:var(--white);color:var(--hero-b)}
.hero-btn.ghost{left:245px;width:142px;border:2px solid var(--white);color:var(--white)}

/* welcome */
.welcome{height:584px}
.kicker{font-family:"Montserrat",sans-serif;font-size:18px;color:var(--ink)}
.sec-title{font-size:33px;font-weight:500;color:var(--ink);line-height:1.15}
.body-text{font-size:13px;line-height:21px;color:var(--muted)}

/* who */
.who{height:560px;background:var(--lavender)}
.stat{position:absolute;left:93px;width:325px;height:139px;border:1.5px solid var(--navy);background:var(--white);text-align:center;padding-top:50px}
.stat-label{font-size:15px;color:var(--ink)}
.stat-num{font-family:"Montserrat",sans-serif;font-weight:800;font-size:28px;color:var(--blue-dark);margin-top:2px}
.stat.featured{left:83px;width:345px;height:146px;background:var(--blue);border:none;box-shadow:0 10px 24px rgba(27,116,204,.35)}
.stat.featured .stat-label,.stat.featured .stat-num{color:var(--white)}

/* services */
.services{height:473px}
.svc{position:absolute;text-align:center;width:300px}
.svc-icon{width:80px;height:80px;margin:0 auto;border-radius:10px;background:linear-gradient(135deg,#cfe0f6,#8fb6e8)}
.svc-name{font-family:"Montserrat",sans-serif;font-size:15px;font-weight:600;margin-top:22px}
.svc-text{font-size:13px;line-height:19px;color:var(--muted);margin-top:14px}
.svc-btn{display:inline-flex;align-items:center;justify-content:center;margin-top:14px;width:106px;height:30px;border-radius:4px;background:var(--blue-dark);color:var(--white);font-size:11px;font-weight:700;font-family:"Montserrat",sans-serif;box-shadow:0 3px 0 var(--navy)}
.svc.featured{background:var(--blue);color:var(--white);width:363px;height:259px;padding:22px 30px;box-shadow:0 12px 30px rgba(27,116,204,.35)}
.svc.featured .svc-icon{background:linear-gradient(135deg,#ffffff,#bcd6f3)}
.svc.featured .svc-text{color:var(--white)}
.svc.featured .svc-btn{background:transparent;border:2px solid var(--white);box-shadow:none}

/* technology */
.tech{height:563px;background:var(--lavender)}
.tech-card{position:absolute;left:502px;top:313px;width:257px;height:194px;background:var(--white);border-top-right-radius:40px;display:flex;flex-direction:column;align-items:center;justify-content:center;gap:14px}
.tech-mark{width:60px;height:60px;border-radius:50%;background:#f2a93b}
.tech-word{font-family:"Montserrat",sans-serif;font-size:33px;letter-spacing:4px;color:var(--navy);font-weight:500}

/* intent */
.intent{height:415px;background:var(--white)}

/* testimonials */
.testi{height:535px;background:var(--lavender)}
.quote{position:absolute;top:137px;width:322px;height:259px;background:var(--blue);border-radius:34px 34px 34px 0;padding:28px 26px 20px 76px;color:var(--white);font-style:italic;font-size:13px;line-height:21px}
.quote::after{content:"";position:absolute;left:40px;bottom:-18px;border-left:0 solid transparent;border-right:22px solid transparent;border-top:18px solid var(--blue)}
.quote-mark{position:absolute;left:20px;top:14px;font-family:"Montserrat",sans-serif;font-size:72px;font-style:normal;font-weight:800;line-height:1}
.who-said{position:absolute;top:427px;display:flex;align-items:center;gap:10px}
.avatar{width:42px;height:42px;border-radius:50%;background:linear-gradient(135deg,#9aa6c3,#4a5575)}
.who-name{font-size:13px;font-weight:600}
.who-role{font-size:10px;color:#8a8fa0}
.dot{position:absolute;top:490px;width:9px;height:9px;border-radius:50%}

/* contact */
.contact{height:633px}
.contact-card{position:absolute;left:157px;top:78px;width:884px;height:483px;background:var(--white);box-shadow:0 10px 40px rgba(40,50,90,.14)}
.contact-panel{position:absolute;left:113px;top:130px;width:306px;height:379px;background:var(--blue-dark);color:var(--white);padding:90px 30px 0}
.contact-panel h3{font-size:20px;font-weight:600;margin-bottom:18px}
.c-row{display:flex;align-items:center;gap:10px;font-size:12px;margin-bottom:12px}
.follow{font-family:"Montserrat",sans-serif;font-size:15px;font-weight:600;margin-top:36px;margin-bottom:14px}
.socials{display:flex;gap:8px}
.social{width:30px;height:30px;border-radius:50%;border:2px solid var(--white)}
.field{position:absolute;height:42px;border:1px solid var(--line);border-radius:22px;padding:0 18px;font-size:13px;color:#6b6f7c;display:flex;align-items:center}
.field.area{height:148px;border-radius:22px;align-items:flex-start;padding-top:14px}
.send{position:absolute;left:859px;top:536px;width:134px;height:42px;border-radius:4px;background:var(--blue-dark);color:var(--white);display:flex;align-items:center;justify-content:center;font-family:"Montserrat",sans-serif;font-weight:700;font-size:14px;box-shadow:0 4px 0 var(--navy)}

/* footer */
.site-footer{height:333px;background:var(--footer);color:#cfd0d6}
.f-brand{position:absolute;left:94px;top:60px;display:flex;align-items:center;gap:10px}
.f-brand .brand-dot{border-color:#e1304c;width:40px;height:40px}
.f-brand span{font-family:"Montserrat",sans-serif;font-weight:600;font-size:22px;color:#e1304c}
.f-tag{position:absolute;left:144px;top:102px;font-size:8px;color:#6fa7e6}
.f-contact{position:absolute;left:94px;top:160px;font-size:12px;line-height:28px}
.f-contact div{display:flex;align-items:center;gap:8px}
.f-col{position:absolute;top:68px;font-size:11px;line-height:24px}
.f-col h4{font-family:"Montserrat",sans-serif;font-size:13px;color:var(--white);font-weight:600;margin-bottom:12px}
.f-socials{display:flex;gap:8px}
.f-socials span{width:26px;height:26px;border-radius:50%;background:var(--white)}
.copy{position:absolute;left:874px;top:240px;font-size:11px}
.copy b{color:#5aa2ee;font-weight:400}
</style>
</head>
<body>

<header class="hero">
  <div class="brand">
    <span class="brand-dot"></span>
    <span class="brand-name">ledgerwisereach</span>
    <span class="brand-tag">The Demand Generation Company</span>
  </div>
  <nav class="nav">
    <span class="active">Home</span><span>About Us</span><span>Our Services</span><span>Prospora &amp; QA Technology</span><span>Intent Data</span><span>Testimonials</span><span>Contact Us</span>
  </nav>
  <p class="hero-kicker">Ledgerwise Reach</p>
  <h1 class="hero-title">The Demand Generation Company</h1>
  <p class="hero-text">Ledgerwise Reach offers multi-channel demand generation services to publishers and technology vendors</p>
  <span class="hero-btn solid">Read More</span>
  <span class="hero-btn ghost">Start a project</span>
  <svg class="hero-curve" viewBox="0 0 1200 120" preserveAspectRatio="none" aria-hidden="true">
    <path d="M0 50 Q600 160 1200 0 L1200 120 L0 120 Z" fill="#ffffff"/>
  </svg>
</header>

<section class="welcome">
  <p class="kicker abs" style="left:94px;top:112px">Welcome to</p>
  <h2 class="sec-title abs" style="left:94px;top:136px">Ledgerwise Reach</h2>
  <p class="body-text abs" style="left:94px;top:186px;width:380px">Ledgerwise Reach offers multi-channel demand generation services to publishers and technology vendors through our network of lead generation websites and native speaking telemarketing agents. Whether looking for MQL, ABM or BANT campaigns, Ledgerwise Reach can assist you in delivering your demand generation strategy and generate pipeline for your sales teams and/or channel partners.</p>
  <span class="btn" style="left:94px;top:352px">Read More</span>
  <div class="frame" style="left:616px;top:64px;width:490px;height:380px"></div>
  <div class="photo" role="img" aria-label="Smiling woman holding a laptop beside a potted plant" style="left:604px;top:72px;width:496px;height:367px;background:linear-gradient(135deg,#d9dbe0,#b8bcc6 60%,#8f9a83)"></div>
  <div class="photo" role="img" aria-label="Hands typing on a laptop in warm light" style="left:502px;top:331px;width:257px;height:191px;border:8px solid #fff;border-top-right-radius:40px;background:linear-gradient(135deg,#d8c6b0,#a88c6e);box-sizing:content-box;margin:-8px"></div>
</section>

<section class="who">
  <div class="stat" style="top:51px"><p class="stat-label">Downloads Per Month</p><p class="stat-num">Ticker to 70,000+</p></div>
  <div class="stat featured" style="top:201px"><p class="stat-label">Leads Delivered Per Month</p><p class="stat-num">Ticker 25,000+</p></div>
  <div class="stat" style="top:360px"><p class="stat-label">Countries We Can Reach</p><p class="stat-num">Ticker to 50+</p></div>
  <h2 class="sec-title abs" style="left:457px;top:44px;font-size:32px">Who We Work With</h2>
  <p class="abs" style="left:457px;top:88px;font-size:14px">QRT, Tarvo, VKD, Halvern, Quillmark, Orvane, Daymere, Cindral, Markwell</p>
  <div class="frame" style="left:470px;top:127px;width:568px;height:376px"></div>
  <div class="photo" role="img" aria-label="Man in glasses working on a laptop in a kitchen" style="left:457px;top:127px;width:573px;height:369px;background:linear-gradient(135deg,#cfd3d4,#7f8a8c 55%,#51625c)"></div>
</section>

<section class="services">
  <h2 class="sec-title abs" style="left:0;width:1200px;text-align:center;top:54px;font-size:31px">Our Services</h2>
  <div class="svc" style="left:102px;top:150px">
    <div class="svc-icon" role="img" aria-label="Megaphone icon"></div>
    <p class="svc-name">Marketing Qualified Leads (MQL)</p>
    <p class="svc-text">A Marketing Qualified Lead (MQL) is a prospect that has expressed an interest in what your brand has to offer.</p>
    <span class="svc-btn">Read More</span>
  </div>
  <div class="svc featured" style="left:417px;top:138px">
    <div class="svc-icon" role="img" aria-label="Account report icon"></div>
    <p class="svc-name">Account Based Marketing Leads (ABM)</p>
    <p class="svc-text">ABM is a strategy that directs marketing resources to engaging a specific set of target accounts.</p>
    <span class="svc-btn">Read More</span>
  </div>
  <div class="svc" style="left:793px;top:150px">
    <div class="svc-icon" role="img" aria-label="Sales person and chart icon"></div>
    <p class="svc-name">Sales Qualified Lead / BANT</p>
    <p class="svc-text">An SQL lead or a BANT lead is a type of lead that expressed a specific interest in a product and service that you have</p>
    <span class="svc-btn">Read More</span>
  </div>
</section>

<section class="tech">
  <h2 class="sec-title abs" style="left:92px;top:52px;font-size:32px">Prospora &amp;<br>QA Technology</h2>
  <p class="body-text abs" style="left:92px;top:136px;width:370px">Prospora is a proprietary lead verification platform from Ledgerwise Reach that aims to sift out invalid leads with questionable or erroneous data. The platform is designed to equip sales teams with accurate, high-quality records in order to improve lead generation, accelerate pipeline and increase revenue. Prospora is positioned to quickly identify, validate, and improve lead quality at the point-of-entry by filtering out all leads that do not match required filters, such as job title, company size, etc. The platform is designed to use real-time contact validation and live phone</p>
  <span class="btn" style="left:94px;top:366px">Read More</span>
  <div class="frame" style="left:616px;top:59px;width:490px;height:369px"></div>
  <div class="photo" role="img" aria-label="Woman in glasses looking at her phone beside a laptop" style="left:604px;top:59px;width:496px;height:360px;background:linear-gradient(135deg,#e4e0da,#b9aa94 55%,#6f7c63)"></div>
  <div class="tech-card">
    <span class="tech-mark"></span>
    <span class="tech-word">PROSPORA</span>
  </div>
</section>

<section class="intent">
  <div class="abs" role="img" aria-label="Hands typing on a laptop with printed charts" style="left:0;top:0;width:707px;height:415px;background:linear-gradient(120deg,#e9ecf1,#c2c8d2 60%,#9aa3b2)"></div>
  <h2 class="sec-title abs" style="left:763px;top:72px;font-size:32px">Intent Data</h2>
  <p class="body-text abs" style="left:763px;top:128px;width:370px">Our relationships with the world's most important technology &amp; business decisions-makers generate a perpetual stream of global data. With access to 35 million individuals and a global behavioural data stream that is authenticated, timely and contextually relevant, we have one of the industry's most powerful signals of buyer intent and can fuel your demand-generation marketing strategies globally</p>
  <span class="btn" style="left:765px;top:318px">Read More</span>
</section>

<section class="testi">
  <p class="abs" style="left:0;width:1200px;text-align:center;top:58px;font-size:12px;color:var(--muted)">What our client says</p>
  <h2 class="sec-title abs" style="left:0;width:1200px;text-align:center;top:76px;font-size:31px">Client Testimonials</h2>
  <div class="quote" style="left:93px"><span class="quote-mark">&ldquo;</span>Lorem ipsum dolor sit aet, coectetur adipiscing elit. Phasellus neque nunc, commodo sit amet libero in, feugiat eleifend nisi. Aenean vel dui at lorem bibendum gravida sit amet nec est. Phasellus a porta lorem. Suspendisse ut diam tempus, sagittis nibh eu, maximus libero. Maecenas id volutpat sapien, eget lobortis mauris.</div>
  <div class="quote" style="left:439px"><span class="quote-mark">&ldquo;</span>Lorem ipsum dolor sit aet, coectetur adipiscing elit. Phasellus neque nunc, commodo sit amet libero in, feugiat eleifend nisi. Aenean vel dui at lorem bibendum gravida sit amet nec est. Phasellus a porta lorem. Suspendisse ut diam tempus, sagittis nibh eu, maximus libero. Maecenas id volutpat sapien, eget lobortis mauris.</div>
  <div class="quote" style="left:784px"><span class="quote-mark">&ldquo;</span>Lorem ipsum dolor sit aet, coectetur adipiscing elit. Phasellus neque nunc, commodo sit amet libero in, feugiat eleifend nisi. Aenean vel dui at lorem bibendum gravida sit amet nec est. Phasellus a porta lorem. Suspendisse ut diam tempus, sagittis nibh eu, maximus libero. Maecenas id volutpat sapien, eget lobortis mauris.</div>
  <div class="who-said" style="left:124px"><span class="avatar" role="img" aria-label="Client portrait"></span><div><p class="who-name">Lorem ipsum</p><p class="who-role">Simply Dummy</p></div></div>
  <div class="who-said" style="left:470px"><span class="avatar" role="img" aria-label="Client portrait"></span><div><p class="who-name">Lorem ipsum</p><p class="who-role">Simply Dummy</p></div></div>
  <div class="who-said" style="left:815px"><span class="avatar" role="img" aria-label="Client portrait"></span><div><p class="who-name">Lorem ipsum</p><p class="who-role">Simply Dummy</p></div></div>
  <span class="dot" style="left:584px;background:var(--blue)"></span>
  <span class="dot" style="left:607px;background:#9cc2ec"></span>
</section>

<section class="contact">
  <div class="contact-card"></div>
  <div class="contact-panel">
    <h3>Contact Us</h3>
    <div class="c-row"><svg width="12" height="14" viewBox="0 0 12 14"><path d="M6 0a5 5 0 0 0-5 5c0 4 5 9 5 9s5-5 5-9a5 5 0 0 0-5-5zm0 7a2 2 0 1 1 0-4 2 2 0 0 1 0 4z" fill="#fff"/></svg>45 BC, making it over 2000</div>
    <div class="c-row"><svg width="13" height="10" viewBox="0 0 13 10"><rect width="13" height="10" rx="1" fill="#fff"/><path d="M0 1l6.5 5L13 1" stroke="#1560ae" fill="none"/></svg>info@ledgerwisereach.example</div>
    <div class="c-row"><svg width="12" height="12" viewBox="0 0 12 12"><path d="M2.5 0l2 3-1.3 1.3a7 7 0 0 0 4.5 4.5L9 7.5l3 2-1.5 2.5C5 12 0 7 0 1.5z" fill="#fff"/></svg>01-123-456-789</div>
    <p class="follow">Follow Us</p>
    <div class="socials"><span class="social"></span><span class="social"></span><span class="social"></span><span class="social"></span><span class="social"></span></div>
  </div>
  <h2 class="sec-title abs" style="left:457px;top:146px;font-size:27px;font-weight:600">Get In Touch</h2>
  <p class="abs" style="left:457px;top:182px;font-size:14px;color:var(--muted)">Feel free to Contact us</p>
  <div class="field" style="left:457px;top:230px;width:270px">First Name</div>
  <div class="field" style="left:730px;top:230px;width:270px">Last Name</div>
  <div class="field" style="left:457px;top:282px;width:270px">Email address</div>
  <div class="field" style="left:730px;top:282px;width:270px">Phone</div>
  <div class="field area" style="left:457px;top:332px;width:543px">Message</div>
  <span class="send">Send Now</span>
</section>

<footer class="site-footer">
  <div class="f-brand"><span class="brand-dot"></span><span>ledgerwisereach</span></div>
  <p class="f-tag">The Demand Generation Company</p>
  <div class="f-contact">
    <div><svg width="10" height="12" viewBox="0 0 12 14"><path d="M6 0a5 5 0 0 0-5 5c0 4 5 9 5 9s5-5 5-9a5 5 0 0 0-5-5z" fill="#fff"/></svg>45 BC, making it over 2000</div>
    <div><svg width="12" height="9" viewBox="0 0 13 10"><rect width="13" height="10" rx="1" fill="#fff"/></svg>info@ledgerwisereach.example</div>
    <div><svg width="11" height="11" viewBox="0 0 12 12"><path d="M2.5 0l2 3-1.3 1.3a7 7 0 0 0 4.5 4.5L9 7.5l3 2-1.5 2.5C5 12 0 7 0 1.5z" fill="#fff"/></svg>01-123-456-789</div>
  </div>
  <div class="f-col" style="left:402px"><h4>Quick Links</h4><p>Home</p><p>About Us</p><p>Our Services</p><p>Prospora &amp; QA Technology</p><p>Intent Data</p><p>Testimonials</p><p>Contact Us</p></div>
  <div class="f-col" style="left:662px;width:180px"><h4>Services</h4><p>Marketing Qualified Leads (MQL)</p><p style="line-height:18px;margin:3px 0">Account Based Marketing Leads (ABM)</p><p>Sales Qualified Lead / BANT</p></div>
  <div class="f-col" style="left:945px"><h4>Follow Us</h4><div class="f-socials"><span></span><span></span><span></span><span></span><span></span></div></div>
  <p class="copy">&copy; 2020 <b>Ledgerwise Reach</b>. All Right Reserved.</p>
</footer>

</body>
</html>
```